Powder Bag Design for supplement company

We need a new bag design for our marine phytoplankton supplement.
we currently have a foil bag with a sticker and we want a full colored design. we are 100% vegan and sustainable. We would want to stick on brand which is a deep blue/purple. (img for reference.) We want a modern updated feel to compete in the market. Playing off of the ocean would be a bonus

Target Market(s)

ages 35+

Industry/Entity Type

health and wellness

```html
<!DOCTYPE html>
<html lang="en">
<head>
<meta charset="UTF-8">
<title>Nerida Phytoplankton Pouch</title>
<link rel="stylesheet" href="https://fonts.googleapis.com/css2?family=Montserrat:wght@300;400;600;700&family=PT+Serif&display=swap">
<style>
  :root {
    --backdrop: #03162c;
    --ocean-deep: #123a66;
    --ocean-mid: #0e6576;
    --ocean-shallow: #14ad9c;
    --zip-line: rgba(8, 30, 58, 0.55);
    --label-silver: #dfe3e6;
    --label-soft: #cfd6da;
  }
  html, body {
    margin: 0;
    padding: 0;
    width: 1200px;
    height: 1000px;
    overflow: hidden;
    background: var(--backdrop);
  }
  .canvas {
    position: relative;
    width: 1200px;
    height: 1000px;
    background: var(--backdrop);
  }
  .pouch {
    position: absolute;
    left: 370px;
    top: 118px;
    width: 470px;
    height: 772px;
    border-radius: 16px;
    overflow: hidden;
  }
  .pouch-art {
    position: absolute;
    inset: 0;
    background:
      radial-gradient(ellipse at 70% 30%, rgba(120, 170, 210, 0.18), transparent 55%),
      radial-gradient(ellipse at 40% 70%, rgba(60, 210, 190, 0.18), transparent 60%),
      linear-gradient(180deg, var(--ocean-deep) 0%, #134a72 25%, var(--ocean-mid) 55%, #11938f 80%, var(--ocean-shallow) 100%);
  }
  .zip-seal {
    position: absolute;
    left: 22px;
    right: 22px;
    top: 70px;
    height: 0;
    border-top: 2px solid var(--zip-line);
  }
  .brand {
    position: absolute;
    left: 0;
    right: 0;
    top: 248px;
    text-align: center;
  }
  .brand-name {
    display: inline-block;
    font-family: "Montserrat", sans-serif;
    font-weight: 400;
    font-size: 86px;
    line-height: 1;
    letter-spacing: 1px;
    color: var(--label-silver);
    position: relative;
  }
  .brand-mark {
    position: absolute;
    right: -22px;
    top: 10px;
    width: 10px;
    height: 10px;
    border-radius: 50%;
    border: 1.5px solid var(--label-silver);
  }
  .brand-tagline {
    margin-top: 14px;
    font-family: "PT Serif", serif;
    font-size: 12.5px;
    letter-spacing: 0.3px;
    color: var(--label-silver);
  }
  .product {
    position: absolute;
    left: 0;
    right: 0;
    top: 456px;
    text-align: center;
    color: var(--label-silver);
  }
  .product-name {
    font-family: "Montserrat", sans-serif;
    font-weight: 700;
    font-size: 25px;
    letter-spacing: 2px;
  }
  .product-claim {
    margin-top: 6px;
    font-family: "Montserrat", sans-serif;
    font-weight: 300;
    font-size: 19px;
    letter-spacing: 1px;
    color: var(--label-soft);
  }
</style>
</head>
<body>
  <main class="canvas">
    <section class="pouch">
      <div class="pouch-art" role="img" aria-label="Rippling ocean water texture in deep blue fading to turquoise"></div>
      <div class="zip-seal"></div>
      <header class="brand">
        <div class="brand-name">Nerida<span class="brand-mark"></span></div>
        <div class="brand-tagline">FOR GOOD HEALTH / POUR UNE BONNE SANTÉ</div>
      </header>
      <div class="product">
        <div class="product-name">PHYTOPLANKTON</div>
        <div class="product-claim">100% Vegan</div>
      </div>
    </section>
  </main>
</body>
</html>
```